CASH PAYMENT DISCOUNT NOTICE POSTED IN CASH REGISTER AREA

LOOKING TO MAKE A FLYER OR A POSTED NOTICE FOR CUSTOMERS PAYING FOR OVER-THE-COUNTER MERCHANDISE AND WHO PAY BY CASH METHOD TO GET A 4% CASH DISCOUNT.
PRESCRIPTIONS ARE EXCLUDED FROM THIS CASH DISCOUNT.

Target Market(s)

RETAIL CUSTOMERS

Industry/Entity Type

RETAIL PHARMACY

Colors
0054AA
0677BA
7BADD7
CADEEF
E8F1F8
EB3D1F
EC4F4E
F09395
F8D3D4
FCEDEE

Requirements
Must have
• LOGO COLORS
Nice to have
• EYE CATCHING

```html
<!DOCTYPE html>
<html lang="en">
<head>
<meta charset="UTF-8">
<title>Cash Discount Notice</title>
<link rel="stylesheet" href="https://fonts.googleapis.com/css2?family=Fredoka:wght@500;600;700&display=swap">
<style>
  :root {
    --brand-blue: #0054AA;
    --brand-red: #EB3D1F;
    --brand-red-soft: #EC4F4E;
    --paper: #FFFFFF;
    --stage: #E8F1F8;
  }
  * { margin: 0; padding: 0; box-sizing: border-box; }
  html, body { width: 1200px; height: 800px; overflow: hidden; background: var(--stage); }
  .notice {
    position: absolute; left: 40px; top: 40px; width: 1120px; height: 720px;
    background: var(--paper); overflow: hidden;
    font-family: "Fredoka", sans-serif;
  }
  .brand {
    position: absolute; left: 120px; top: 82px;
    display: flex; align-items: center; gap: 16px;
  }
  .brand-mark { width: 34px; height: 34px; background: var(--brand-blue); }
  .brand-name { font-weight: 600; font-size: 50px; color: var(--brand-red); letter-spacing: 0.5px; }
  .notice-tag {
    position: absolute; left: 690px; top: 98px;
    font-weight: 700; font-size: 56px; color: var(--brand-blue); letter-spacing: -1px;
  }
  .megaphone {
    position: absolute; left: 905px; top: 82px; width: 112px; height: 112px;
    background: linear-gradient(135deg, var(--brand-red), var(--brand-red-soft));
    border-radius: 12px;
  }
  .get {
    position: absolute; left: 110px; top: 222px;
    font-weight: 700; font-size: 52px; line-height: 1; color: var(--brand-red);
  }
  .rate {
    position: absolute; left: 140px; top: 215px;
    font-weight: 700; font-size: 310px; line-height: 1; color: var(--brand-blue); letter-spacing: -8px;
  }
  .cash {
    position: absolute; left: 740px; top: 250px;
    font-weight: 600; font-size: 120px; line-height: 1; color: var(--brand-blue); letter-spacing: -2px;
  }
  .discount-ribbon {
    position: absolute; left: 720px; top: 385px; width: 360px; height: 120px;
    background: var(--brand-red);
    clip-path: polygon(0 0, 100% 0, 97% 20%, 100% 40%, 97% 60%, 100% 80%, 100% 100%, 0 100%, 3% 80%, 0 60%, 3% 40%, 0 20%);
    display: flex; align-items: center; justify-content: center;
    font-weight: 700; font-size: 68px; color: var(--paper); letter-spacing: 1px;
  }
  .rule { position: absolute; left: 0; top: 540px; width: 100%; height: 10px; background: var(--brand-red); }
  .terms {
    position: absolute; left: 0; top: 550px; width: 100%; height: 170px;
    background: var(--brand-blue);
    display: flex; align-items: center; justify-content: center;
    text-align: center; color: var(--paper);
    font-weight: 600; font-size: 40px; line-height: 1.3;
  }
</style>
</head>
<body>
  <main class="notice">
    <div class="brand">
      <span class="brand-mark"></span>
      <span class="brand-name">Larkin Pharmacy</span>
    </div>
    <div class="notice-tag">NOTICE</div>
    <div class="megaphone" role="img" aria-label="Megaphone illustration announcing the notice"></div>
    <div class="get">GET</div>
    <div class="rate">4%</div>
    <div class="cash">CASH</div>
    <div class="discount-ribbon">DISCOUNT</div>
    <div class="rule"></div>
    <div class="terms">PRESCRIPTIONS ARE EXCLUDED FROM<br>THIS CASH DISCOUNT</div>
  </main>
</body>
</html>
```